CPA Firm Business Card
Halvorin, Bestwick & Pardue CPAs, LLC
Project: CPA Firm Business Card
CPA Firm Business Card - Financial Services
Creative Brief
Professional
Moss Brandley, CPA
2867 E. Sable Way, Suite 348 Tucson, AZ 85619
moss@quillledger.net
In addition to business cards design I would also like to see designs for letterheads, envelopes and fax cover sheets.

```html
<!DOCTYPE html>
<html lang="en">
<head>
<meta charset="utf-8">
<title>Halvorin, Bestwick &amp; Pardue CPAs, LLC – Business Card</title>
<link rel="stylesheet" href="https://fonts.googleapis.com/css2?family=Roboto+Condensed:wght@400;700&family=Roboto:ital,wght@0,400;1,400;1,500&display=swap">
<style>
  :root {
    --backdrop: #e9e9eb;
    --card: #ffffff;
    --card-shadow: rgba(0, 0, 0, 0.18);
    --brand-red: #8c1b24;
    --brand-red-deep: #6e1219;
    --swoosh-grey: #c9c9cc;
    --ink: #3a3a3c;
    --ink-soft: #6d6d70;
    --ghost: #ececee;
  }
  * { box-sizing: border-box; margin: 0; padding: 0; }
  html, body { width: 1200px; height: 980px; overflow: hidden; }
  body {
    background: var(--backdrop);
    position: relative;
    font-family: "Roboto", Arial, sans-serif;
  }
  .card {
    position: absolute;
    width: 560px;
    height: 320px;
    background: var(--card);
    border-radius: 22px;
    overflow: hidden;
    box-shadow: 0 14px 30px var(--card-shadow);
  }
  .card--back { left: 590px; top: 170px; }
  .card--front { left: 60px; top: 500px; }

  /* back */
  .back__name-mark {
    position: absolute;
    right: 36px;
    top: 78px;
    font-family: "Roboto Condensed", Arial, sans-serif;
    font-weight: 700;
    font-size: 46px;
    line-height: 1.05;
    color: var(--ghost);
    text-transform: uppercase;
    text-align: right;
  }
  .back__web {
    position: absolute;
    left: 36px;
    top: 120px;
    font-style: italic;
    font-size: 15px;
    letter-spacing: 2px;
    color: var(--ink-soft);
  }

  /* front */
  .front__waves { position: absolute; inset: 0; }
  .firm-name {
    position: absolute;
    left: 40px;
    top: 34px;
    display: flex;
    align-items: center;
    gap: 14px;
  }
  .firm-name__square {
    width: 46px;
    height: 46px;
    background: var(--brand-red);
    flex: none;
  }
  .firm-name__text {
    font-family: "Roboto Condensed", Arial, sans-serif;
    font-weight: 700;
    font-size: 22px;
    line-height: 1.1;
    color: var(--brand-red);
    text-transform: uppercase;
  }
  .person {
    position: absolute;
    left: 40px;
    top: 108px;
    font-style: italic;
    font-weight: 500;
    font-size: 13px;
    color: var(--brand-red);
  }
  .contact {
    position: absolute;
    left: 370px;
    top: 188px;
    list-style: none;
    font-size: 11px;
    line-height: 19px;
    color: var(--ink);
  }
  .contact li { display: flex; align-items: center; gap: 8px; }
  .contact__icon {
    width: 12px;
    height: 12px;
    border-radius: 50%;
    background: var(--ink);
    flex: none;
  }
  .contact__spacer { width: 12px; flex: none; }
</style>
</head>
<body>

<section class="card card--back" aria-label="Business card back">
  <div class="back__name-mark">Halvorin<br>Bestwick<br>Pardue</div>
  <p class="back__web">www.quillledger.net</p>
</section>

<section class="card card--front" aria-label="Business card front">
  <svg class="front__waves" width="560" height="320" viewBox="0 0 560 320" aria-hidden="true">
    <path d="M0,138 C110,126 190,150 250,210 C290,252 330,296 400,320 L380,320 C320,300 280,262 240,222 C180,166 100,146 0,152 Z" fill="var(--swoosh-grey)"/>
    <path d="M0,156 C100,148 170,170 225,228 C260,266 290,304 330,320 L0,320 Z" fill="var(--brand-red)"/>
    <path d="M0,250 C80,240 150,262 210,320 L0,320 Z" fill="var(--brand-red-deep)" opacity="0.35"/>
  </svg>

  <div class="firm-name">
    <span class="firm-name__square"></span>
    <span class="firm-name__text">Halvorin, Bestwick<br>&amp; Pardue CPAs, LLC</span>
  </div>

  <p class="person">Moss Brandley, CPA</p>

  <ul class="contact">
    <li><span class="contact__icon"></span>2867 E. Sable Way, Suite 348</li>
    <li><span class="contact__spacer"></span>Tucson, AZ 85619</li>
    <li><span class="contact__icon"></span>520-555-0148</li>
    <li><span class="contact__icon"></span>520-555-0192</li>
    <li><span class="contact__icon"></span>moss@quillledger.net</li>
    <li><span class="contact__icon"></span>www.quillledger.net</li>
  </ul>
</section>

</body>
</html>
```